professional business card design

Business card design. Photos have been uploaded and i am open to the designer choosing which photos to use. Would like the card to be mostyly in a grey scale design with black, whites, silver & grey colours. I have added copy of our flyer as would like on the back side of card our services to be listed. Do not use any bright colurs such as blue red green or yellow. i need to be able to edit the phone number and naem in the final card design submitted.

Target Market(s)

Clients

Industry/Entity Type

earhmovibng and transport

Contact Information for Business Card

Director Name, address, email, phone number and services

Colors

Designer to choose only greyscale colors for use in the design.

Requirements
Should not have
• no yellow, red, blue or green

```html
<!DOCTYPE html>
<html lang="en">
<head>
<meta charset="utf-8">
<title>IHS Business Card</title>
<link href="https://fonts.googleapis.com/css2?family=Roboto+Condensed:wght@400;700&display=swap" rel="stylesheet">
<style>
  :root {
    --page-bg: #d9dadc;
    --silver-light: #f4f4f5;
    --silver-mid: #c9cacc;
    --silver-dark: #8e9093;
    --ink: #141414;
    --black: #0b0b0b;
    --text-dark: #1e1e1e;
    --text-soft: #3a3a3a;
    --logo-grey: #4a4b4d;
  }
  * { box-sizing: border-box; margin: 0; padding: 0; }
  html, body { width: 1200px; height: 846px; overflow: hidden; }
  body {
    background: var(--page-bg);
    font-family: "Roboto Condensed", Arial, sans-serif;
    color: var(--text-dark);
    position: relative;
  }
  .card {
    position: absolute;
    width: 520px;
    height: 318px;
    border-radius: 22px;
    overflow: hidden;
    background: linear-gradient(160deg, var(--silver-light) 0%, var(--silver-mid) 55%, var(--silver-light) 100%);
    box-shadow: 0 10px 24px rgba(0,0,0,0.22);
  }
  .card--front { left: 50px; top: 264px; }
  .card--back { left: 630px; top: 264px; }
  .card__swoosh { position: absolute; inset: 0; width: 100%; height: 100%; }
  .photo {
    position: absolute;
    border-radius: 6px;
  }
  .photo--front {
    left: 250px; top: 40px; width: 240px; height: 190px;
    background: linear-gradient(135deg, #e6e6e7 0%, #9a9b9e 45%, #3b3c3e 100%);
  }
  .photo--back {
    left: 110px; top: 160px; width: 250px; height: 140px;
    background: linear-gradient(120deg, #cfcfd1 0%, #555658 45%, #1b1b1c 100%);
  }
  .brand {
    position: absolute;
    font-weight: 700;
    color: var(--logo-grey);
    letter-spacing: 2px;
    line-height: 1;
  }
  .card--front .brand { left: 28px; top: 30px; font-size: 62px; }
  .card--back .brand { right: 34px; bottom: 50px; font-size: 64px; color: var(--silver-mid); }
  .person { position: absolute; left: 40px; top: 108px; }
  .person__name { font-weight: 700; font-size: 19px; color: var(--text-dark); }
  .person__role { font-size: 15px; color: var(--text-soft); margin-bottom: 8px; }
  .contacts { list-style: none; font-size: 14.5px; color: var(--text-dark); }
  .contacts li { display: flex; align-items: flex-start; gap: 8px; line-height: 1.25; margin-bottom: 2px; }
  .contacts svg { width: 14px; height: 14px; flex: none; margin-top: 2px; fill: var(--ink); }
  .services {
    position: absolute;
    list-style: none;
    font-size: 14px;
    line-height: 1.22;
    color: var(--text-dark);
  }
  .services li { padding-left: 9px; text-indent: -9px; }
  .services li::before { content: "• "; }
  .services--one { left: 30px; top: 48px; width: 150px; }
  .services--two { left: 190px; top: 36px; width: 160px; }
  .services--three { left: 360px; top: 24px; width: 150px; }
</style>
</head>
<body>

<section class="card card--front" aria-label="Front of business card">
  <svg class="card__swoosh" viewBox="0 0 520 318" preserveAspectRatio="none" aria-hidden="true">
    <defs>
      <linearGradient id="bandFront" x1="0" y1="0" x2="1" y2="0">
        <stop offset="0" stop-color="#fafafa"/>
        <stop offset="0.5" stop-color="#9b9c9f"/>
        <stop offset="1" stop-color="#e8e8e9"/>
      </linearGradient>
    </defs>
    <path d="M0 300 C170 292 230 275 265 190 C300 100 350 72 520 68 L520 318 L0 318 Z" fill="url(#bandFront)"/>
    <path d="M0 312 C180 306 245 290 280 205 C315 118 365 90 520 88 L520 318 L0 318 Z" fill="var(--black)"/>
  </svg>
  <div class="photo photo--front" role="img" aria-label="Photo of a road train prime mover with bull bar"></div>
  <div class="brand">IHS</div>
  <div class="person">
    <p class="person__name">Daniel Reeve</p>
    <p class="person__role">director</p>
    <ul class="contacts">
      <li><svg viewBox="0 0 24 24"><path d="M6.6 10.8a15 15 0 0 0 6.6 6.6l2.2-2.2a1 1 0 0 1 1-.25 11.4 11.4 0 0 0 3.6.57 1 1 0 0 1 1 1V20a1 1 0 0 1-1 1A17 17 0 0 1 3 4a1 1 0 0 1 1-1h3.5a1 1 0 0 1 1 1c0 1.25.2 2.45.57 3.57a1 1 0 0 1-.25 1z"/></svg>Tel. 000 555 000</li>
      <li><svg viewBox="0 0 24 24"><path d="M2 5h20v14H2z M3 6l9 7 9-7" fill="none" stroke="#141414" stroke-width="2"/></svg>email@ironbarkhaul.com.au</li>
      <li><svg viewBox="0 0 24 24"><circle cx="12" cy="12" r="10"/><path d="M2 12h20M12 2c3 3 3 17 0 20M12 2c-3 3-3 17 0 20" stroke="#e0e0e0" stroke-width="1.5" fill="none"/></svg>www.ironbarkhaul.com.au</li>
      <li><svg viewBox="0 0 24 24"><path d="M12 2a7 7 0 0 0-7 7c0 5 7 13 7 13s7-8 7-13a7 7 0 0 0-7-7zm0 9.5A2.5 2.5 0 1 1 12 6.5a2.5 2.5 0 0 1 0 5z"/></svg>Lot 114, Ridge Creek Road,<br>Opal Flats, Australia</li>
    </ul>
  </div>
</section>

<section class="card card--back" aria-label="Back of business card">
  <svg class="card__swoosh" viewBox="0 0 520 318" preserveAspectRatio="none" aria-hidden="true">
    <defs>
      <linearGradient id="bandBack" x1="0" y1="0" x2="1" y2="0">
        <stop offset="0" stop-color="#fafafa"/>
        <stop offset="0.6" stop-color="#9b9c9f"/>
        <stop offset="1" stop-color="#e8e8e9"/>
      </linearGradient>
    </defs>
    <path d="M0 300 C200 296 290 270 330 190 C365 115 390 90 520 82 L520 318 L0 318 Z" fill="url(#bandBack)"/>
    <path d="M0 312 C210 308 300 285 345 205 C380 135 405 108 520 104 L520 318 L0 318 Z" fill="var(--black)"/>
  </svg>
  <div class="photo photo--back" role="img" aria-label="Photo of a prime mover hauling a tipper trailer"></div>
  <ul class="services services--one">
    <li>Over size loads / Hot Shot Loads</li>
    <li>Heavy Vehicle Recovery Services</li>
    <li>Portable Water Deliveries</li>
  </ul>
  <ul class="services services--two">
    <li>Road Building / Maintenance</li>
    <li>Sand &amp; Metal Supply &amp; Cartage</li>
    <li>Earthworks</li>
    <li>Drop Deck Trailers</li>
  </ul>
  <ul class="services services--three">
    <li>Road Train Tippers</li>
    <li>Road Train Tankers</li>
    <li>Road Train Flat Tops</li>
    <li>Mine Site Accredited Equipment &amp; Operators</li>
  </ul>
  <div class="brand">IHS</div>
</section>

</body>
</html>
```